Eastfield Commercial Card

I would like a modern, eye catching card based off my logo design.
Info to include:
Anders Voll (Card Name)
eastfieldcommercial.example (Website)
555 203 8841 (Office/fax)
555 287 3096 (Business Cell)
anders@eastfieldcommercial.example (Work email)

Target Market(s)

Commercial real estate brokers, property owners.

Colors
ec1f27
757575

Requirements
Must have
• Name and info above. Not be lame!:)

```html
<!DOCTYPE html>
<html lang="en">
<head>
<meta charset="utf-8">
<title>Eastfield Commercial Card</title>
<link rel="stylesheet" href="https://fonts.googleapis.com/css2?family=Montserrat:wght@600&family=Open+Sans:wght@400&display=swap">
<style>
  :root {
    --red: #ec1f27;
    --grey: #757575;
    --stage: #141414;
    --card-top: #262626;
    --card-bottom: #1c1c1c;
    --text-light: #d9d9d9;
    --rule: #3a3a3a;
  }
  * { box-sizing: border-box; margin: 0; padding: 0; }
  html, body {
    width: 1200px; height: 900px; overflow: hidden;
    background: var(--stage);
  }
  .stage {
    position: relative; width: 1200px; height: 900px;
  }
  .card {
    position: absolute; left: 300px; width: 600px; height: 343px;
    border-radius: 22px;
    background: linear-gradient(160deg, var(--card-top), var(--card-bottom));
    box-shadow: 0 14px 40px rgba(0,0,0,.6);
    overflow: hidden;
  }
  .card--back { top: 90px; }
  .card--front { top: 467px; }

  /* back */
  .back-brand {
    position: absolute; left: 60px; top: 118px;
    display: flex; align-items: center; gap: 12px;
  }
  .brand-mark { width: 22px; height: 22px; }
  .back-brand .brand-mark { background: #fff; }
  .brand-name {
    font-family: "Montserrat", sans-serif; font-weight: 600;
    text-transform: uppercase; letter-spacing: 1px;
  }
  .back-brand .brand-name { color: #fff; font-size: 30px; }
  .back-rule {
    position: absolute; left: 60px; right: 60px; top: 200px;
    height: 1px; background: var(--rule);
  }
  .back-web {
    position: absolute; left: 0; right: 0; top: 222px; text-align: center;
    font-family: "Open Sans", sans-serif; font-size: 16px; color: var(--text-light);
  }

  /* front */
  .front-brand {
    position: absolute; right: 48px; top: 66px;
    display: flex; align-items: center; gap: 10px;
  }
  .front-brand .brand-mark { background: var(--grey); width: 18px; height: 18px; }
  .front-brand .brand-name { color: var(--red); font-size: 22px; }
  .front-rule {
    position: absolute; left: 40px; right: 40px; top: 150px;
    height: 1px; background: var(--rule);
  }
  .person {
    position: absolute; left: 48px; top: 190px;
  }
  .person-name {
    font-family: "Montserrat", sans-serif; font-weight: 600;
    color: var(--red); font-size: 22px; text-transform: uppercase;
    letter-spacing: .5px; padding-bottom: 8px;
    border-bottom: 1px solid var(--rule); margin-bottom: 10px;
  }
  .contact-list { list-style: none; }
  .contact-list li {
    display: flex; align-items: center; gap: 10px;
    font-family: "Open Sans", sans-serif; font-size: 16px;
    color: var(--text-light); line-height: 25px;
  }
  .contact-list--right {
    position: absolute; right: 48px; top: 206px;
  }
  .contact-list--right li { justify-content: flex-end; }
  .icon { width: 14px; height: 14px; flex: none; }
</style>
</head>
<body>
<main class="stage">

  <section class="card card--back" aria-label="Card back">
    <div class="back-brand">
      <span class="brand-mark"></span>
      <span class="brand-name">Eastfield Commercial</span>
    </div>
    <div class="back-rule"></div>
    <p class="back-web">www.eastfieldcommercial.example</p>
  </section>

  <section class="card card--front" aria-label="Card front">
    <div class="front-brand">
      <span class="brand-mark"></span>
      <span class="brand-name">Eastfield Commercial</span>
    </div>
    <div class="front-rule"></div>

    <div class="person">
      <h1 class="person-name">Anders Voll</h1>
      <ul class="contact-list">
        <li>
          <svg class="icon" viewBox="0 0 14 14"><rect x="3" y="1" width="8" height="12" rx="1.5" fill="none" stroke="var(--red)" stroke-width="1.6"/><circle cx="7" cy="10.8" r=".9" fill="var(--red)"/></svg>
          555 287 3096
        </li>
        <li>
          <svg class="icon" viewBox="0 0 14 14"><path d="M3 2 L5.5 2 L6.5 5 L5 6.2 Q6.5 8.8 8 9.2 L9.2 7.7 L12 8.8 L12 11.2 Q6 12.5 2.5 5 Z" fill="var(--red)"/></svg>
          555 203 8841
        </li>
        <li>
          <svg class="icon" viewBox="0 0 14 14"><rect x="1" y="5" width="12" height="8" rx="1.5" fill="var(--red)"/><rect x="4" y="1" width="6" height="5" fill="none" stroke="var(--red)" stroke-width="1.4"/></svg>
          555 203 8841
        </li>
      </ul>
    </div>

    <ul class="contact-list contact-list--right">
      <li>
        anders@eastfieldcommercial.example
        <svg class="icon" viewBox="0 0 14 14"><rect x="1" y="3" width="12" height="8" rx="1" fill="var(--red)"/><path d="M1.5 3.5 L7 8 L12.5 3.5" fill="none" stroke="#1f1f1f" stroke-width="1.2"/></svg>
      </li>
      <li>
        www.eastfieldcommercial.example
        <svg class="icon" viewBox="0 0 14 14"><circle cx="7" cy="7" r="6" fill="var(--red)"/><path d="M1 7 H13 M7 1 Q3.5 7 7 13 M7 1 Q10.5 7 7 13" fill="none" stroke="#1f1f1f" stroke-width="1"/></svg>
      </li>
    </ul>
  </section>

</main>
</body>
</html>
```